Business card on Pvc transparent frosted

I need a business advertising card that will be eye catching and fun.
Target Market(s)
Rednecks, country, hunters, Fisherman, ATV users, lifted trucks, cowboys, cattle ranchers, farmers, etc
Industry/Entity Type
Apparel Store
Contact Information for Business Card
This will he printed on single side of a transparent frosted plastic card with shinny foil print option.
Requirements
Must have
- 1 - My logo.
- 2 - HOLLER BOOTSTRAP OUTFITTERS
- 3 - my motto "DONT judge how we look..... Judge the WILD mess we make!!"; 4 - my website "hollerbootstrap@mailvex.example"

Nice to have
- Use your imagination with negative space, partial graffics, etc. Keep in mind you can kind of see through the card

Should not have
- Do not change colors of chevrons

```html
<!DOCTYPE html>
<html lang="en">
<head>
<meta charset="utf-8">
<title>Holler Bootstrap Outfitters – Business Card</title>
<link href="https://fonts.googleapis.com/css2?family=Roboto:wght@400;500;700&display=swap" rel="stylesheet">
<style>
  :root {
    --page-bg: #d9d4cc;
    --card-frost: #eeebe6;
    --card-edge: #f8f6f2;
    --ink: #2b2b2b;
    --brand-red: #c8141c;
    --gold-light: #d9b437;
    --gold-dark: #b38b1c;
    --divider: #4a4a4a;
  }
  * { box-sizing: border-box; margin: 0; padding: 0; }
  html, body {
    width: 1200px; height: 1047px; overflow: hidden;
    background: var(--page-bg);
    font-family: "Roboto", Arial, sans-serif;
    color: var(--ink);
  }
  .card {
    position: absolute; left: 120px; top: 264px;
    width: 960px; height: 520px;
    border-radius: 24px;
    background: linear-gradient(160deg, var(--card-edge), var(--card-frost));
    border: 2px solid rgba(255,255,255,0.8);
    box-shadow: 0 18px 40px rgba(0,0,0,0.18);
    overflow: hidden;
  }
  .brand {
    position: absolute; left: 83px; top: 170px; width: 320px;
    display: flex; flex-direction: column; align-items: center; gap: 18px;
  }
  .brand-mark { width: 46px; height: 46px; background: var(--brand-red); }
  .brand-name {
    font-weight: 700; font-size: 30px; line-height: 1.15;
    text-align: center; color: var(--ink); letter-spacing: 0.5px;
  }
  .divider {
    position: absolute; left: 440px; top: 121px;
    width: 2px; height: 270px; background: var(--divider);
  }
  .contact-block { position: absolute; left: 485px; top: 134px; }
  .person-name {
    font-weight: 700; font-size: 40px; color: var(--brand-red);
    letter-spacing: 0.5px; line-height: 1;
  }
  .person-role { font-size: 25px; margin-top: 8px; font-weight: 400; }
  .contact-list { list-style: none; margin-top: 54px; }
  .contact-list li {
    display: flex; align-items: center; gap: 12px;
    font-size: 25px; height: 39px; letter-spacing: 0.3px;
  }
  .contact-list svg { width: 18px; height: 18px; fill: var(--brand-red); flex: none; }
  .motto-rule {
    position: absolute; left: 0; top: 448px; width: 100%; height: 8px;
    border-top: 3px solid var(--brand-red); border-bottom: 2px solid var(--brand-red);
  }
  .motto-band {
    position: absolute; left: 0; top: 456px; width: 100%; height: 64px;
    background: linear-gradient(90deg, var(--gold-dark), var(--gold-light) 45%, var(--gold-dark));
    display: flex; align-items: center; justify-content: center;
  }
  .motto { font-weight: 700; font-size: 23px; color: var(--ink); letter-spacing: 0.3px; }
</style>
</head>
<body>
  <div class="card">
    <div class="brand">
      <div class="brand-mark"></div>
      <div class="brand-name">HOLLER BOOTSTRAP<br>OUTFITTERS</div>
    </div>

    <div class="divider"></div>

    <div class="contact-block">
      <h1 class="person-name">DALTON REEVES</h1>
      <p class="person-role">Managing Director</p>
      <ul class="contact-list">
        <li>
          <svg viewBox="0 0 24 24" aria-hidden="true"><path d="M6.6 10.8a15.2 15.2 0 0 0 6.6 6.6l2.2-2.2a1 1 0 0 1 1-.25 11.4 11.4 0 0 0 3.6.57 1 1 0 0 1 1 1V20a1 1 0 0 1-1 1A17 17 0 0 1 3 4a1 1 0 0 1 1-1h3.5a1 1 0 0 1 1 1c0 1.25.2 2.45.57 3.57a1 1 0 0 1-.25 1z"/></svg>
          +1 000 000 0000
        </li>
        <li>
          <svg viewBox="0 0 24 24" aria-hidden="true"><path d="M2 5h20v2l-10 6L2 7z M2 9l10 6 10-6v10H2z"/></svg>
          hollerbootstrap@mailvex.example
        </li>
        <li>
          <svg viewBox="0 0 24 24" aria-hidden="true"><path d="M12 2a10 10 0 1 0 0 20 10 10 0 0 0 0-20zm6.9 6h-3a15.6 15.6 0 0 0-1.4-3.6A8 8 0 0 1 18.9 8zM12 4c.8 1.2 1.5 2.5 1.9 4h-3.8c.4-1.5 1.1-2.8 1.9-4zM4.3 14a8 8 0 0 1 0-4h3.4a16.5 16.5 0 0 0 0 4zm.8 2h3a15.6 15.6 0 0 0 1.4 3.6A8 8 0 0 1 5.1 16zm3-8h-3a8 8 0 0 1 4.4-3.6A15.6 15.6 0 0 0 8.1 8zM12 20c-.8-1.2-1.5-2.5-1.9-4h3.8c-.4 1.5-1.1 2.8-1.9 4zm2.3-6H9.7a14.7 14.7 0 0 1 0-4h4.6a14.7 14.7 0 0 1 0 4zm.2 5.6a15.6 15.6 0 0 0 1.4-3.6h3a8 8 0 0 1-4.4 3.6zm1.8-5.6a16.5 16.5 0 0 0 0-4h3.4a8 8 0 0 1 0 4z"/></svg>
          www.hollerbootstrap.example
        </li>
      </ul>
    </div>

    <div class="motto-rule"></div>
    <div class="motto-band">
      <p class="motto">DONT judge how we look..... Judge the WILD mess we make!!</p>
    </div>
  </div>
</body>
</html>
```